Bref créative
Business Cards/Stationary for a Consulting Company
Darvey Solutions
Simple
Lorette Darvey
PO BOX 4087
Cedar Vale, AZ 85999
lorette@darveysolutions-example.com
www.darveysolutions-example.com

```html
<!DOCTYPE html>
<html lang="en">
<head>
<meta charset="utf-8">
<title>Darvey Solutions — Business Card</title>
<link rel="stylesheet" href="https://fonts.googleapis.com/css2?family=Tinos:wght@400;700&display=swap">
<style>
  :root {
    --backdrop: #d9d9d9;
    --card: #ffffff;
    --brand-blue: #1f4f9f;
    --brand-blue-light: #3f86d6;
    --ink: #2b2b2b;
    --muted: #555555;
    --band-dark: #3a3a3a;
    --divider: #b9b9b9;
  }
  * { box-sizing: border-box; margin: 0; padding: 0; }
  html, body { width: 1200px; height: 871px; overflow: hidden; }
  body {
    background: var(--backdrop);
    font-family: "Tinos", "Times New Roman", serif;
    color: var(--ink);
    position: relative;
  }
  .card {
    position: absolute;
    width: 540px;
    height: 309px;
    background: var(--card);
    box-shadow: 0 6px 18px rgba(0,0,0,0.18);
    overflow: hidden;
  }
  .card--back { left: 40px; top: 281px; }
  .card--front { left: 620px; top: 281px; }

  /* back */
  .back-mark {
    position: absolute; left: 0; right: 0; top: 70px;
    display: flex; flex-direction: column; align-items: center; gap: 18px;
  }
  .brand-dot {
    width: 88px; height: 88px; border-radius: 50%;
    background: var(--brand-blue);
  }
  .back-name {
    font-size: 26px; color: var(--brand-blue); letter-spacing: 1px;
  }
  .back-url {
    font-size: 13px; color: var(--muted); letter-spacing: 2px;
  }

  /* front */
  .brand {
    position: absolute; left: 38px; top: 42px;
    display: flex; align-items: center; gap: 12px;
  }
  .brand .brand-dot { width: 58px; height: 58px; }
  .brand-name { font-size: 27px; color: var(--brand-blue); letter-spacing: 0.5px; }

  .person {
    position: absolute; right: 265px; top: 160px; text-align: right;
  }
  .person-name {
    font-size: 17px; color: var(--brand-blue);
    font-variant: small-caps; letter-spacing: 0.5px;
  }
  .person-title { font-size: 13px; color: var(--ink); margin-top: 2px; }

  .divider {
    position: absolute; left: 288px; top: 148px; width: 1px; height: 96px;
    background: var(--divider);
  }
  .contact {
    position: absolute; left: 300px; top: 150px;
    font-size: 11.5px; line-height: 16px; color: var(--ink);
  }
  .contact .gap { height: 10px; }
  .contact-line { display: flex; align-items: center; gap: 5px; }
  .contact-line svg { width: 10px; height: 10px; fill: var(--ink); flex: none; }

  .band-blue {
    position: absolute; left: 0; bottom: 14px; width: 320px; height: 14px;
    background: linear-gradient(90deg, var(--brand-blue), var(--brand-blue-light));
    clip-path: polygon(0 0, 100% 0, 94% 100%, 0 100%);
  }
  .band-dark {
    position: absolute; right: 0; bottom: 0; width: 240px; height: 28px;
    background: var(--band-dark);
    clip-path: polygon(6% 0, 100% 0, 100% 100%, 0 100%);
    display: flex; align-items: center; justify-content: flex-end;
    padding-right: 12px;
  }
  .band-dark span { color: #ffffff; font-size: 11.5px; letter-spacing: 0.3px; }
</style>
</head>
<body>
  <section class="card card--back" aria-label="Card back">
    <div class="back-mark">
      <div class="brand-dot"></div>
      <div class="back-name">Darvey Solutions</div>
      <div class="back-url">www.darveysolutions-example.com</div>
    </div>
  </section>

  <section class="card card--front" aria-label="Card front">
    <div class="brand">
      <div class="brand-dot"></div>
      <div class="brand-name">Darvey Solutions</div>
    </div>

    <div class="person">
      <div class="person-name">Lorette Darvey</div>
      <div class="person-title">Managing Director</div>
    </div>

    <div class="divider"></div>

    <div class="contact">
      <div>PO BOX 4087</div>
      <div>Cedar Vale, AZ 85999</div>
      <div class="gap"></div>
      <div class="contact-line">
        <svg viewBox="0 0 10 10" aria-hidden="true"><path d="M2 0.5 L3.6 2.6 L2.8 3.6 Q4 6 6.4 7.2 L7.4 6.4 L9.5 8 L8.4 9.5 Q2 8.5 0.5 1.6 Z"/></svg>
        <span>480-555-0148</span>
      </div>
      <div class="contact-line">
        <svg viewBox="0 0 10 10" aria-hidden="true"><path d="M0.5 2 H9.5 V8.5 H0.5 Z M1.2 2.6 L5 5.6 L8.8 2.6 V7.9 H1.2 Z" fill-rule="evenodd"/></svg>
        <span>lorette@darveysolutions-example.com</span>
      </div>
    </div>

    <div class="band-blue"></div>
    <div class="band-dark"><span>www.darveysolutions-example.com</span></div>
  </section>
</body>
</html>
```